looking to have a web site for the company which provides services in the industrial and commercial sectors such as: electrical, automation control and system integration, construction and maintenance, millwright, equipment assembly repair and installation. I have the domain already brivanholdings.net and logo. Most recent projects fulfilled for the following clients: MarlowKibbleCo, Dunholt University, OKSU, FALSTO, Tazzik, Prairie Grains

Target Market(s)

industrial and commercial sectors in electrical, automation, millwright and fabrication fields

Industry/Entity Type

Industrial

Coding

Coded - Design and coding required

Number of Pages Required

5+ page

Font styles to use
Sans Serif

Colors

Designer to choose colors to be used in the design.

Requirements
Nice to have
• looking to get something not complicated, nicely presented with minimum or no scrolling

```html
<!DOCTYPE html>
<html lang="en">
<head>
<meta charset="utf-8">
<title>Brivan Holdings Ltd</title>
<link href="https://fonts.googleapis.com/css2?family=Poppins:wght@300;400;500;600&family=Roboto:wght@300;400;500&display=swap" rel="stylesheet">
<style>
:root{
  --blue:#0b66a8;
  --blue-bright:#1f8fd6;
  --ink:#333a40;
  --muted:#6b7278;
  --light:#f2f2f2;
  --grey:#e9e9e9;
  --white:#ffffff;
  --footer:#1b1d20;
  --footer-bar:#0c0d0e;
  --footer-text:#a7abaf;
}
*{margin:0;padding:0;box-sizing:border-box}
html,body{width:1200px;height:2875px;overflow:hidden}
body{position:relative;background:var(--white);font-family:'Roboto',sans-serif;color:var(--ink)}
.abs{position:absolute}
.heading{font-family:'Poppins',sans-serif}

/* header */
.site-header{position:absolute;left:0;top:0;width:1200px;height:77px;background:var(--white)}
.brand{position:absolute;left:153px;top:14px;display:flex;align-items:center;gap:10px;font-family:'Poppins',sans-serif;font-weight:600;color:#4a6a86;line-height:1}
.brand-mark{width:30px;height:30px;background:#4a6a86}
.brand-name{font-size:22px;letter-spacing:1px}
.brand-name small{display:block;font-size:12px;letter-spacing:5px;margin-top:5px}
.main-nav{position:absolute;top:30px;left:532px;display:flex;gap:0;font-family:'Poppins',sans-serif;font-size:12.5px;color:#333}
.main-nav a{color:inherit;text-decoration:none;position:absolute;white-space:nowrap}
.main-nav a.active{color:var(--blue-bright)}
.main-nav a.active::after{content:"";position:absolute;left:0;right:0;bottom:-8px;height:2px;background:var(--blue-bright)}

/* hero */
.hero{position:absolute;left:0;top:77px;width:1200px;height:485px;background:linear-gradient(120deg,#6f6c68 0%,#a9a49c 35%,#8c8579 60%,#5d5a57 100%)}
.hero-caption{position:absolute;left:600px;top:134px;width:399px;height:197px;background:rgba(18,18,18,.82);padding:28px 28px}
.hero-caption h1{font-family:'Poppins',sans-serif;font-weight:400;font-size:29px;color:var(--white);line-height:1}
.hero-caption h1 span{color:var(--blue-bright);font-weight:500}
.hero-caption p{font-size:11.5px;line-height:16px;color:#eee;margin-top:16px}
.hero-arrow{position:absolute;top:188px;width:35px;height:72px;background:rgba(30,30,30,.55)}
.hero-arrow svg{position:absolute;left:9px;top:24px}

/* about */
.about{position:absolute;left:0;top:562px;width:1200px;height:439px;background:var(--light)}
.about .eyebrow{position:absolute;left:151px;top:80px;font-family:'Poppins',sans-serif;font-size:21px;font-weight:300;color:#444}
.about h2{position:absolute;left:151px;top:110px;font-family:'Poppins',sans-serif;font-weight:400;font-size:30px;color:#333}
.blue{color:var(--blue)}
.about p{position:absolute;left:151px;top:162px;width:435px;font-size:10.8px;line-height:16px;color:var(--muted)}
.about-photo{position:absolute;left:608px;top:82px;width:442px;height:257px;background:linear-gradient(180deg,#c9d4dc 0%,#9ea6a6 55%,#6e7a5e 100%)}

.btn{position:absolute;display:flex;align-items:center;justify-content:center;background:var(--blue);color:var(--white);font-family:'Poppins',sans-serif;font-weight:500;font-size:10.5px;letter-spacing:.3px}

/* services */
.services{position:absolute;left:0;top:1001px;width:1200px;height:567px;background:var(--grey)}
.section-title{position:absolute;left:0;width:1200px;text-align:center;font-family:'Poppins',sans-serif;font-size:28px;font-weight:400;color:#333}
.section-title span{color:var(--blue);font-weight:500}
.service-card{position:absolute;top:92px;width:287px}
.service-photo{width:287px;height:180px}
.service-card h3{margin-top:22px;font-family:'Poppins',sans-serif;font-size:12.5px;font-weight:500;color:var(--blue);line-height:16px;height:34px}
.service-card p{margin-top:6px;font-size:10.8px;line-height:14px;color:var(--muted)}
.service-card .btn{position:static;width:102px;height:32px;margin-top:18px}
.btn-outline{position:absolute;left:497px;top:481px;width:207px;height:35px;border:1.5px solid var(--blue);display:flex;align-items:center;justify-content:center;font-family:'Poppins',sans-serif;font-size:12px;font-weight:500;color:var(--blue);letter-spacing:.5px}

/* industry */
.industry{position:absolute;left:0;top:1568px;width:1200px;height:487px;background:var(--light)}
.industry-photo{position:absolute;left:0;top:0;width:600px;height:487px;background:linear-gradient(135deg,#4f5557 0%,#8e9496 40%,#b8bcbc 55%,#5a6062 100%)}
.industry h2{position:absolute;left:682px;top:108px;font-family:'Poppins',sans-serif;font-size:29px;font-weight:500;color:var(--blue)}
.industry .lead{position:absolute;left:682px;top:152px;width:380px;font-size:14px;line-height:19px;color:#333}
.industry .body{position:absolute;left:682px;top:201px;width:368px;font-size:10.8px;line-height:15.5px;color:var(--muted)}

/* testimonials */
.testimonials{position:absolute;left:0;top:2055px;width:1200px;height:422px;background:var(--grey)}
.testimonial{position:absolute;top:90px;width:286px}
.quote-box{position:relative;height:190px;background:var(--blue);border-radius:6px;padding:20px 20px}
.quote-box p{margin-top:14px;font-size:10.8px;line-height:15.5px;color:var(--white)}
.quote-box .q-open{position:absolute;left:18px;top:20px}
.quote-box .q-close{position:absolute;right:18px;bottom:16px}
.quote-box::after{content:"";position:absolute;left:72px;bottom:-16px;border-left:0 solid transparent;border-right:24px solid transparent;border-top:16px solid var(--blue)}
.avatar{position:absolute;left:0;top:165px;width:63px;height:63px;border-radius:50%;border:3px solid var(--white);background:linear-gradient(180deg,#b9a99a,#7b6d63)}
.person{position:absolute;left:95px;top:202px;font-family:'Poppins',sans-serif;font-size:11.5px;font-weight:500;color:#222}
.person small{display:block;font-family:'Roboto',sans-serif;font-weight:400;font-size:9.5px;color:var(--muted);margin-top:1px}
.dots{position:absolute;left:576px;top:366px;display:flex;gap:8px}
.dots i{width:10px;height:10px;border-radius:50%;border:1.5px solid var(--blue)}
.dots i.on{background:var(--blue)}

/* footer */
.site-footer{position:absolute;left:0;top:2477px;width:1200px;height:360px;background:linear-gradient(180deg,#222426,#17191b)}
.footer-col h4{position:absolute;font-family:'Poppins',sans-serif;font-size:12px;font-weight:500;color:var(--white)}
.sitemap{position:absolute;left:150px;top:116px;list-style:none}
.sitemap li{font-size:11.5px;color:var(--footer-text);line-height:24.5px}
.sitemap li::before{content:"›";margin-right:9px;color:var(--footer-text)}
.contact-list{position:absolute;left:309px;top:114px;list-style:none}
.contact-list li{display:flex;align-items:center;gap:10px;font-size:11.5px;color:var(--footer-text);line-height:24.5px}
.social{position:absolute;left:309px;top:243px;display:flex;gap:9px}
.social i{width:25px;height:25px;border-radius:4px;background:#3b5a9a}
.social i:nth-child(2){border-radius:50%;background:#3d9ad6}
.social i:nth-child(3){background:#2a76ad}
.social i:nth-child(4){border-radius:50%;background:#d24a3c}
.field{position:absolute;height:27px;border:1px solid #4a4d50;background:rgba(0,0,0,.2);font-size:11px;color:#8a8e92;padding:7px 8px}
.send{position:absolute;left:968px;top:218px;width:82px;height:29px;background:var(--blue);color:var(--white);font-family:'Poppins',sans-serif;font-size:11.5px;font-weight:500;display:flex;align-items:center;justify-content:center}
.footer-bar{position:absolute;left:0;top:2837px;width:1200px;height:38px;background:var(--footer-bar);text-align:center;font-size:10.5px;line-height:38px;color:#8d9194}
.footer-bar b{color:var(--white);font-weight:500}
</style>
</head>
<body>

<header class="site-header">
  <div class="brand"><span class="brand-mark"></span><span class="brand-name">BRIVAN<small>HOLDINGS LTD</small></span></div>
  <nav class="main-nav">
    <a class="active" style="left:0">Home</a>
    <a style="left:81px">About</a>
    <a style="left:161px">Services</a>
    <a style="left:252px">Industry</a>
    <a style="left:342px">Testimonials</a>
    <a style="left:459px">Contact us</a>
  </nav>
</header>

<section class="hero" role="img" aria-label="Photo of industrial feed processing machinery in a warehouse">
  <div class="hero-arrow" style="left:151px"><svg width="16" height="24" viewBox="0 0 16 24"><path d="M12 2 3 12l9 10" fill="none" stroke="#fff" stroke-width="1.6"/></svg></div>
  <div class="hero-arrow" style="left:1014px"><svg width="16" height="24" viewBox="0 0 16 24"><path d="M4 2l9 10-9 10" fill="none" stroke="#fff" stroke-width="1.6"/></svg></div>
  <div class="hero-caption">
    <h1><span>BRIVAN</span> HOLDINGS LTD</h1>
    <p>Nunc pretium scelerisque nisi, vitae convallis nulla efficitur ac. Donec non neque id ante scelerisque laoreet. Quisque mollis ex euismod, pretium metus ac, volutpat. Sed ullamcorper tempus est ac lobortis. Curabitur nec leo ut urna sodales condimentum nec in libero.</p>
  </div>
</section>

<section class="about">
  <div class="eyebrow">About</div>
  <h2><span class="blue">BRIVAN</span> HOLDINGS LTD</h2>
  <p>Lorem ipsum dolor sit amet, consectetur adipiscing elit. In non mollis nulla. Nullam mollis elit ligula, eu iaculis erat aliquet ut. Nullam lectus sapien, vestibulum ac venenatis vel, facilisis tristique lacus. Donec in ipsum vulputate, vulputate sem id, iaculis lacus. Suspendisse lacinia mauris consectetur dolor egestas commodo. Nulla lobortis leo sed nisi finibus rhoncus. Praesent dui dolor, imperdiet a ornare non, cursus vitae nunc. Pellentesque id consectetur felis. Sed vel vehicula tortor. Suspendisse viverra erat augue, ac tincidunt eros auctor id.</p>
  <div class="btn" style="left:150px;top:308px;width:99px;height:31px">READ MORE</div>
  <div class="about-photo" role="img" aria-label="Photo of grain silos and an industrial plant under a cloudy sky"></div>
</section>

<section class="services">
  <h2 class="section-title" style="top:32px"><span>OUR</span> SERVICES</h2>
  <article class="service-card" style="left:151px">
    <div class="service-photo" role="img" aria-label="Photo of an electrical disconnect switch panel" style="background:linear-gradient(135deg,#9a9a96,#c8c6c0 50%,#7d7b78)"></div>
    <h3>Electrical</h3>
    <p>Aliquam varius, leo ac aliquet fringilla, urna sapien tie odio, et vulputate dui felis et leo. Aliquam et malesuada nibh. Vivamus sit amet bibendum nunc.</p>
    <div class="btn">READ MORE</div>
  </article>
  <article class="service-card" style="left:458px">
    <div class="service-photo" role="img" aria-label="Photo of an automation control cabinet with breakers and wiring" style="background:linear-gradient(135deg,#6e6e6e,#b7b4ae 50%,#8c4a3a 80%,#777)"></div>
    <h3>Automation Control and System Integration</h3>
    <p>Aliquam varius, leo ac aliquet fringilla, urna sapien tie odio, et vulputate dui felis et leo. Aliquam et malesuada nibh. Vivamus sit amet bibendum nunc.</p>
    <div class="btn">READ MORE</div>
  </article>
  <article class="service-card" style="left:764px">
    <div class="service-photo" role="img" aria-label="Photo of construction and maintenance work on plant piping" style="background:linear-gradient(135deg,#c9c0a0,#8b8f86 45%,#4f6a86 75%,#a09a82)"></div>
    <h3>Construction and Maintenance</h3>
    <p>Aliquam varius, leo ac aliquet fringilla, urna sapien tie odio, et vulputate dui felis et leo. Aliquam et malesuada nibh. Vivamus sit amet bibendum nunc.</p>
    <div class="btn">READ MORE</div>
  </article>
  <div class="btn-outline">VIEW ALL SERVICES</div>
</section>

<section class="industry">
  <div class="industry-photo" role="img" aria-label="Photo of stainless steel process tanks and equipment in a plant"></div>
  <h2>INDUSTRY</h2>
  <p class="lead">Fusce efficitur lectus et ante porta, sodales ultricies purus eleifend. Suspendisse arcu purus</p>
  <p class="body">Etiam ac tempor metus, nec pretium diam. Integer in aliquet odio. Praesent quis congue quam. Nullam libero sem, tincidunt a nisl quis, sollicitudin malesuada erat. Aliquam luctus pellentesque lobortis. Curabitur non enim ut orci posuere sodales. Proin a magna leo. Curabitur pulvinar nisl sed justo faucibus ornare. Ut et fermentum enim. Vestibulum vel porttitor dui, in facilisis magna. Quisque semper augue in tortor placerat, vel vestibulum sem laoreet.</p>
  <div class="btn" style="left:682px;top:345px;width:99px;height:31px">READ MORE</div>
</section>

<section class="testimonials">
  <h2 class="section-title" style="top:30px"><span>CLIENT</span> TESTIMONIALS</h2>

  <article class="testimonial" style="left:151px">
    <div class="quote-box">
      <svg class="q-open" width="34" height="22" viewBox="0 0 34 22"><path d="M2 22V12C2 5 6 1 12 0v4c-3 1-5 3-5 7h5v11zM20 22V12c0-7 4-11 10-12v4c-3 1-5 3-5 7h5v11z" fill="#fff"/></svg>
      <p style="margin-top:26px">Aliquam et malesuada nibh. Vivamus sit amet biben nunc, at dapibus nulla. Maecenas sollicitudin pellen quam. Duis placerat aliquam eros eu. Ut eu mollis lacus. Nam nec luctus nibh, snunc.</p>
      <svg class="q-close" width="34" height="22" viewBox="0 0 34 22"><path d="M32 0v10c0 7-4 11-10 12v-4c3-1 5-3 5-7h-5V0zM14 0v10c0 7-4 11-10 12v-4c3-1 5-3 5-7H4V0z" fill="#fff"/></svg>
    </div>
    <div class="avatar" role="img" aria-label="Client portrait photo"></div>
    <div class="person">Lorem ipsum<small>Dolor sit amet</small></div>
  </article>

  <article class="testimonial" style="left:458px">
    <div class="quote-box">
      <svg class="q-open" width="34" height="22" viewBox="0 0 34 22"><path d="M2 22V12C2 5 6 1 12 0v4c-3 1-5 3-5 7h5v11zM20 22V12c0-7 4-11 10-12v4c-3 1-5 3-5 7h5v11z" fill="#fff"/></svg>
      <p style="margin-top:26px">Aliquam et malesuada nibh. Vivamus sit amet biben nunc, at dapibus nulla. Maecenas sollicitudin pellen quam. Duis placerat aliquam eros eu. Ut eu mollis lacus. Nam nec luctus nibh, snunc.</p>
      <svg class="q-close" width="34" height="22" viewBox="0 0 34 22"><path d="M32 0v10c0 7-4 11-10 12v-4c3-1 5-3 5-7h-5V0zM14 0v10c0 7-4 11-10 12v-4c3-1 5-3 5-7H4V0z" fill="#fff"/></svg>
    </div>
    <div class="avatar" role="img" aria-label="Client portrait photo" style="background:linear-gradient(180deg,#d9d6d2,#9a948e)"></div>
    <div class="person">Fusce efficitur<small>Dolor sit amet</small></div>
  </article>

  <article class="testimonial" style="left:764px">
    <div class="quote-box">
      <svg class="q-open" width="34" height="22" viewBox="0 0 34 22"><path d="M2 22V12C2 5 6 1 12 0v4c-3 1-5 3-5 7h5v11zM20 22V12c0-7 4-11 10-12v4c-3 1-5 3-5 7h5v11z" fill="#fff"/></svg>
      <p style="margin-top:26px">Aliquam et malesuada nibh. Vivamus sit amet biben nunc, at dapibus nulla. Maecenas sollicitudin pellen quam. Duis placerat aliquam eros eu. Ut eu mollis lacus. Nam nec luctus nibh, snunc.</p>
      <svg class="q-close" width="34" height="22" viewBox="0 0 34 22"><path d="M32 0v10c0 7-4 11-10 12v-4c3-1 5-3 5-7h-5V0zM14 0v10c0 7-4 11-10 12v-4c3-1 5-3 5-7H4V0z" fill="#fff"/></svg>
    </div>
    <div class="avatar" role="img" aria-label="Client portrait photo" style="background:linear-gradient(180deg,#e2d3c8,#8a6f62)"></div>
    <div class="person">Mauris facilisis<small>Dolor sit amet</small></div>
  </article>

  <div class="dots"><i class="on"></i><i></i><i></i></div>
</section>

<footer class="site-footer">
  <div class="footer-col">
    <h4 style="left:150px;top:88px">Sitemap</h4>
    <ul class="sitemap">
      <li>Home</li><li>About</li><li>Services</li><li>Industry</li><li>Testimonials</li><li>Contact us</li>
    </ul>
  </div>
  <div class="footer-col">
    <h4 style="left:309px;top:88px">Contact Us</h4>
    <ul class="contact-list">
      <li><svg width="12" height="14" viewBox="0 0 12 14"><path d="M6 0a5 5 0 0 0-5 5c0 4 5 9 5 9s5-5 5-9a5 5 0 0 0-5-5zm0 7a2 2 0 1 1 0-4 2 2 0 0 1 0 4z" fill="#2d8fd5"/></svg>45 BC, making it over 2000</li>
      <li><svg width="12" height="14" viewBox="0 0 12 14"><path d="M2 1l3 0 1 3-2 1.5c1 2 2 3 4 4L9.5 8l3 1v3c-6 1-12-5-11-11z" fill="#2d8fd5"/></svg>01-555-010-274</li>
      <li><svg width="12" height="14" viewBox="0 0 12 14"><rect x="0" y="3" width="12" height="8" fill="#2d8fd5"/><path d="M0 3l6 5 6-5" fill="none" stroke="#1b1d20" stroke-width="1"/></svg>info@brivanholdings.net</li>
      <li><svg width="12" height="14" viewBox="0 0 12 14"><circle cx="6" cy="7" r="5.3" fill="none" stroke="#2d8fd5" stroke-width="1.3"/><path d="M1 7h10M6 1.7c-2.5 3-2.5 7.6 0 10.6M6 1.7c2.5 3 2.5 7.6 0 10.6" fill="none" stroke="#2d8fd5" stroke-width="1"/></svg>www.brivanholdings.net</li>
    </ul>
    <h4 style="left:309px;top:217px">Follow Us</h4>
    <div class="social"><i></i><i></i><i></i><i></i></div>
  </div>
  <div class="footer-col">
    <h4 style="left:533px;top:88px">Get in Touch</h4>
    <div class="field" style="left:537px;top:113px;width:249px">First Name</div>
    <div class="field" style="left:796px;top:113px;width:254px">Last Name</div>
    <div class="field" style="left:537px;top:145px;width:249px">Email Id</div>
    <div class="field" style="left:796px;top:145px;width:254px">Phone</div>
    <div class="field" style="left:537px;top:178px;width:513px">Comment</div>
    <div class="send">SEND</div>
  </div>
</footer>
<div class="footer-bar">© 2017 <b>BRIVAN HOLDINGS LTD</b> . All right reserved</div>

</body>
</html>
```